RLT PowerPoint

I am looking for a clean, corporate PowerPoint template.

I would like the following:
- title slide
- break slide
- blank slide with title (for graphs or graphics)
- an ending slide.

Target Market(s)

Business professionals, medium to large business clients.

Requirements
Must have
• Must incorporate the RLT logo in either the header or footer

```html
<!DOCTYPE html>
<html lang="en">
<head>
<meta charset="utf-8">
<title>RLT Title Slide</title>
<link href="https://fonts.googleapis.com/css2?family=Source+Sans+3:wght@400;600;700&display=swap" rel="stylesheet">
<style>
  :root {
    --brand-blue: #1b55a4;
    --header-bg: #ffffff;
    --stage-bg: #ebebeb;
    --title-grey: #878787;
    --footer-text: #ffffff;
  }
  html, body {
    margin: 0;
    padding: 0;
    overflow: hidden;
  }
  .slide {
    position: relative;
    width: 1200px;
    height: 875px;
    overflow: hidden;
    background: var(--stage-bg);
    font-family: "Source Sans 3", "Myriad Pro", sans-serif;
  }
  .stage-texture {
    position: absolute;
    left: 0;
    top: 116px;
    width: 1200px;
    height: 736px;
    display: block;
  }
  .slide-header {
    position: absolute;
    top: 0;
    left: 0;
    width: 1200px;
    height: 116px;
    background: var(--header-bg);
    display: flex;
    align-items: center;
    justify-content: center;
    gap: 14px;
  }
  .brand-mark {
    width: 40px;
    height: 40px;
    background: var(--brand-blue);
  }
  .brand-name {
    margin: 0;
    color: var(--brand-blue);
    font-size: 40px;
    font-weight: 700;
    letter-spacing: 0.5px;
    line-height: 1;
  }
  .title-block {
    position: absolute;
    right: 411px;
    top: 412px;
    text-align: right;
    color: var(--title-grey);
  }
  .slide-title {
    margin: 0;
    font-size: 60px;
    font-weight: 400;
    line-height: 1;
  }
  .slide-subtitle {
    margin: 5px 0 0;
    font-size: 30px;
    font-weight: 400;
    line-height: 1;
  }
  .slide-footer {
    position: absolute;
    left: 0;
    bottom: 0;
    width: 1200px;
    height: 23px;
    background: var(--brand-blue);
  }
  .version-label {
    position: absolute;
    right: 17px;
    top: 5px;
    margin: 0;
    color: var(--footer-text);
    font-size: 13px;
    font-weight: 600;
    line-height: 1;
  }
</style>
</head>
<body>
  <div class="slide">
    <svg class="stage-texture" width="1200" height="736" aria-hidden="true">
      <filter id="paper-grain" x="0" y="0" width="100%" height="100%">
        <feTurbulence type="fractalNoise" baseFrequency="0.95" numOctaves="2" seed="7" result="grain"/>
        <feColorMatrix in="grain" type="matrix"
          values="0.6 0 0 0 0.2
                  0 0.6 0 0 0.2
                  0 0 0.6 0 0.22
                  0 0 0 0 0.14"/>
      </filter>
      <rect width="1200" height="736" fill="#ebebeb"/>
      <rect width="1200" height="736" filter="url(#paper-grain)"/>
    </svg>
    <header class="slide-header">
      <span class="brand-mark" aria-hidden="true"></span>
      <p class="brand-name">RLT&nbsp;&nbsp;ROWAN LANE TRUST</p>
    </header>
    <main class="title-block">
      <h1 class="slide-title">Title Goes Here</h1>
      <p class="slide-subtitle">Sub-title goes here</p>
    </main>
    <footer class="slide-footer">
      <p class="version-label">version 1.0</p>
    </footer>
  </div>
</body>
</html>
```